Design home page for SME Tidewell

WordPress homepage for SME Tidewell.
Will use GeneratePress, and the theme will be a child theme of Generate Press.
Logo attached.
SME Tidewell is a business that advises Small to Medium Businesses towards success.

```html
<!DOCTYPE html>
<html lang="en">
<head>
<meta charset="utf-8">
<title>SME Tidewell – Business Advisory for Small to Medium Businesses</title>
<link href="https://fonts.googleapis.com/css2?family=Poppins:wght@400;500;600;700;800&display=swap" rel="stylesheet">
<style>
:root{
  --slate:#728092;
  --slate-dark:#5f6c7d;
  --slate-soft:#a3adb9;
  --ink:#1f2530;
  --text:#4a4f57;
  --muted:#8a9099;
  --panel:#f4f4f5;
  --line:#d9dce0;
  --white:#ffffff;
  --footer:#1f2733;
  --footer-text:#b9c0ca;
}
*{box-sizing:border-box;margin:0;padding:0}
html,body{width:1200px;height:4068px;overflow:hidden}
body{position:relative;background:var(--white);font-family:'Poppins',sans-serif;color:var(--text)}
.abs{position:absolute}
.shapes{position:absolute;left:0;top:0;width:1200px;height:4068px}

/* header */
.topbar{left:88px;top:0;width:1022px;height:66px;background:var(--white)}
.brand{display:flex;align-items:center;gap:10px}
.brand-mark{width:30px;height:30px;background:var(--slate)}
.brand-name{font-weight:500;font-size:30px;letter-spacing:1px;color:var(--ink);line-height:1}
.header-brand{left:126px;top:14px}
.info{font-size:11px;color:var(--muted);line-height:1.2}
.info b{display:block;font-size:15px;color:var(--ink);font-weight:600}
.info-icon{width:22px;height:22px;border:1.5px solid var(--slate-soft);border-radius:50%}
.navbar{left:98px;top:66px;width:1004px;height:41px;background:var(--slate);border-radius:0 0 22px 22px}
.nav a{position:absolute;top:80px;font-size:13px;font-weight:600;color:var(--white);text-decoration:none;letter-spacing:.3px}
.phone-pill{left:932px;top:72px;width:142px;height:28px;background:var(--slate-dark);border-radius:4px;color:var(--white);font-size:12px;font-weight:500;display:flex;align-items:center;justify-content:center;gap:6px;transform:skewX(-12deg)}
.phone-pill span{transform:skewX(12deg);display:flex;align-items:center;gap:6px}

/* hero */
.hero-kicker{left:88px;top:322px;font-size:40px;font-weight:700;color:var(--white)}
.hero-title{left:86px;top:362px;font-size:60px;font-weight:800;color:var(--white);line-height:1.1}
.hero-sub{left:88px;top:443px;width:420px;font-size:17px;color:var(--white);line-height:1.35}
.btn-light{left:90px;top:505px;width:163px;height:41px;background:var(--white);color:var(--ink);font-size:13px;font-weight:600;display:flex;align-items:center;justify-content:center;clip-path:polygon(6% 0,100% 0,94% 100%,0 100%)}

/* about */
.eyebrow{font-size:22px;color:var(--slate);font-weight:500}
.h2{font-size:35px;font-weight:700;color:var(--ink);line-height:1.18}
.body-copy{font-size:13.5px;line-height:22px;color:var(--text)}
.btn-outline{width:136px;height:41px;border:1.5px solid var(--ink);font-size:13px;font-weight:600;color:var(--ink);display:flex;align-items:center;justify-content:center;transform:skewX(-10deg)}
.btn-outline span{transform:skewX(10deg)}

/* services */
.section-title{left:0;width:1200px;text-align:center;font-size:35px;font-weight:700;color:var(--ink);line-height:41px}
.service{width:310px;text-align:center}
.service h3{font-size:17px;font-weight:600;color:var(--ink);margin-top:0}
.service p{font-size:13px;line-height:21px;margin-top:12px;color:var(--text);padding:0 38px}
.service.is-active h3,.service.is-active p{color:var(--white)}

/* stats */
.stat-num{font-size:36px;font-weight:800;color:var(--slate);line-height:1}
.stat-label{font-size:17px;color:var(--text);margin-top:2px}

/* news */
.news-title{font-size:22px;font-weight:700;color:var(--white);line-height:25px}
.news-desc{font-size:13px;color:#e8ebef;line-height:21px;margin-top:8px}
.news-more{font-size:16px;font-weight:700;color:var(--slate-soft);margin-top:2px}

/* partners */
.partner{top:3316px;width:196px;height:79px;border:1px solid var(--line);display:flex;align-items:center;justify-content:center;gap:8px;font-size:18px;font-weight:600;color:#6d737c}
.partner i{width:20px;height:20px;border-radius:50%;background:#9aa1ab;display:block}

/* cta */
.cta-text{left:250px;top:3546px;font-size:28px;font-weight:700;color:var(--white);line-height:29px}
.cta-btn{left:797px;top:3553px;width:198px;height:41px;background:var(--white);color:var(--ink);font-size:13px;font-weight:600;display:flex;align-items:center;justify-content:center;clip-path:polygon(5% 0,100% 0,95% 100%,0 100%)}

/* footer */
.footer-brand{left:82px;top:3800px}
.footer-brand .brand-name{color:var(--white)}
.footer-brand .brand-mark{background:var(--slate-soft)}
.f-head{font-size:22px;font-weight:600;color:var(--white)}
.f-list{font-size:14px;line-height:22px;color:var(--footer-text);list-style:none}
.f-input{left:583px;top:3818px;width:246px;height:41px;border-radius:21px;background:#323b48;color:#e3e7ec;font-size:13px;display:flex;align-items:center;padding-left:22px}
.social{left:898px;top:3910px;display:flex;gap:12px}
.social i{width:10px;height:10px;border-radius:50%;background:var(--white);display:block}
.copyright{left:0;top:4032px;width:1200px;text-align:center;font-size:14px;color:var(--white)}
.to-top{left:1121px;top:3995px;width:38px;height:38px;border-radius:50%;background:var(--slate)}
</style>
</head>
<body>

<svg class="shapes" viewBox="0 0 1200 4068" aria-hidden="false">
  <!-- hero photo -->
  <path role="img" aria-label="Photo of two colleagues smiling at a tablet in an office" d="M650 100 H1200 V690 Q1188 800 1090 803 H430 Z" fill="#b7a692"/>
  <!-- hero panel -->
  <path d="M0 0 H650 L432 760 Q410 829 335 829 H0 Z" fill="var(--slate)"/>
  <circle cx="95" cy="290" r="100" fill="#ffffff" opacity=".08"/>

  <!-- about photo -->
  <path role="img" aria-label="Photo of a business team applauding" d="M150 958 H520 Q545 958 538 990 L482 1345 Q476 1378 445 1378 H195 Q165 1378 160 1350 L120 990 Q116 958 150 958 Z" fill="#c9a474"/>

  <!-- service cards -->
  <path d="M222 1568 H415 Q428 1568 432 1582 L474 1860 Q476 1877 458 1877 H180 Q162 1877 164 1860 L206 1582 Q210 1568 222 1568 Z" fill="#fff" stroke="#eceef1"/>
  <path d="M1001 1568 H808 Q795 1568 791 1582 L723 1860 Q721 1877 739 1877 H1018 Q1036 1877 1034 1860 L1017 1582 Q1013 1568 1001 1568 Z" fill="#fff" stroke="#eceef1"/>

  <!-- consultants panel -->
  <path d="M145 1855 H1200 V2487 H115 V1890 Q115 1855 145 1855 Z" fill="var(--panel)"/>
  <path d="M476 1560 H735 Q753 1560 753 1580 V1858 Q753 1877 735 1877 H508 Q490 1877 487 1858 L444 1580 Q441 1560 476 1560 Z" fill="var(--slate)"/>
  <path d="M690 2150 L1180 2100 Q1200 2100 1200 2120 V2520 L698 2460 Q668 2456 668 2430 V2175 Q668 2152 690 2150 Z" fill="#c5c8cd"/>
  <path role="img" aria-label="Photo of a team working together around a meeting table" d="M698 2037 L1200 1939 V2507 L698 2416 Z" fill="#9a8573"/>

  <!-- stats divider -->
  <rect x="88" y="2662" width="1023" height="1.5" fill="var(--line)"/>

  <!-- news photos -->
  <rect x="88" y="2825" width="514" height="383" rx="10" fill="#6b7584" role="img" aria-label="Photo of two colleagues in a bright office meeting"/>
  <rect x="616" y="2825" width="238" height="383" rx="10" fill="#5c6470" role="img" aria-label="Photo of a smiling businesswoman"/>
  <rect x="868" y="2825" width="240" height="383" rx="10" fill="#566c86" role="img" aria-label="Photo of a smiling man and woman"/>
  <defs>
    <linearGradient id="shade" x1="0" y1="0" x2="0" y2="1">
      <stop offset="0" stop-color="#1f2733" stop-opacity="0"/>
      <stop offset="1" stop-color="#1f2733" stop-opacity=".85"/>
    </linearGradient>
  </defs>
  <rect x="88" y="2960" width="514" height="248" rx="10" fill="url(#shade)"/>
  <rect x="616" y="2960" width="238" height="248" rx="10" fill="url(#shade)"/>
  <rect x="868" y="2960" width="240" height="248" rx="10" fill="url(#shade)"/>

  <!-- footer -->
  <path d="M0 3760 Q0 3576 110 3576 H1090 Q1200 3576 1200 3760 V4068 H0 Z" fill="var(--footer)"/>
  <rect x="0" y="4010" width="1200" height="1" fill="#39424f"/>
  <!-- cta -->
  <path d="M205 3505 H1010 Q1030 3505 1033 3525 L1045 3625 Q1047 3640 1030 3640 H168 Q150 3640 153 3625 L182 3525 Q186 3505 205 3505 Z" fill="var(--slate)"/>

  <!-- service icons -->
  <g fill="none" stroke="#7b8491" stroke-width="2">
    <rect x="287" y="1632" width="64" height="44"/><line x1="319" y1="1624" x2="319" y2="1632"/><line x1="300" y1="1676" x2="294" y2="1692"/><line x1="338" y1="1676" x2="344" y2="1692"/>
    <circle cx="304" cy="1650" r="8"/><polyline points="318,1664 328,1652 336,1658 346,1642"/>
  </g>
  <g fill="none" stroke="#ffffff" stroke-width="2">
    <rect x="570" y="1660" width="8" height="14"/><rect x="582" y="1652" width="8" height="22"/><rect x="594" y="1644" width="8" height="30"/>
    <polyline points="570,1644 585,1632 596,1638 610,1626"/><circle cx="610" cy="1664" r="11"/><line x1="618" y1="1672" x2="630" y2="1686"/>
  </g>
  <g fill="none" stroke="#7b8491" stroke-width="2">
    <circle cx="856" cy="1640" r="12"/><path d="M860 1634 Q852 1631 851 1637 Q851 1641 857 1641 Q862 1642 861 1646 Q858 1650 851 1646 M856 1629 V1652"/>
    <rect x="846" y="1666" width="7" height="20"/><rect x="858" y="1658" width="7" height="28"/><rect x="870" y="1648" width="7" height="38"/><rect x="882" y="1636" width="7" height="50"/>
    <polyline points="872,1640 884,1622 892,1632"/>
  </g>

  <!-- header icons -->
  <g fill="none" stroke="var(--slate-soft)" stroke-width="1.5">
    <path d="M696 22 a7 7 0 0 1 14 0 c0 6 -7 14 -7 14 s-7 -8 -7 -14z"/><circle cx="703" cy="22" r="2.5"/>
    <circle cx="916" cy="34" r="13"/><polyline points="916,26 916,34 922,38"/>
  </g>
  <!-- footer icons -->
  <g fill="var(--footer-text)">
    <path d="M876 3794 a5 5 0 0 1 10 0 c0 4 -5 10 -5 10 s-5 -6 -5 -10z"/>
    <rect x="876" y="3812" width="9" height="9" rx="2"/>
  </g>
  <path d="M788 3839 L802 3832 L798 3846 L795 3840 Z" fill="#9aa3ae"/>
  <polyline points="1133,4018 1140,4011 1147,4018" fill="none" stroke="#fff" stroke-width="2"/>
</svg>

<!-- header -->
<header>
  <div class="abs brand header-brand"><span class="brand-mark"></span><span class="brand-name">SME TIDEWELL</span></div>
  <div class="abs info" style="left:718px;top:17px">Address<b>Some goes address</b></div>
  <div class="abs info" style="left:943px;top:17px">Monday – Friday<b>Monday – Friday</b></div>
  <div class="abs navbar"></div>
  <nav class="nav">
    <a style="left:150px">HOME</a>
    <a style="left:210px">ABOUT US</a>
    <a style="left:310px">SERVICES</a>
    <a style="left:406px">PORTFOLIO</a>
    <a style="left:511px">BLOG</a>
    <a style="left:579px">CONTACT US</a>
  </nav>
  <div class="abs phone-pill"><span>&#9742; 123 4567 000</span></div>
</header>

<!-- hero -->
<section>
  <div class="abs hero-kicker">Welcome to</div>
  <h1 class="abs hero-title">SME Tidewell</h1>
  <p class="abs hero-sub">Is a business that advises Small to Medium Businesses towards success.</p>
  <div class="abs btn-light">VIEW SERVICES</div>
</section>

<!-- about -->
<section>
  <div class="abs eyebrow" style="left:594px;top:1044px">About Us</div>
  <h2 class="abs h2" style="left:591px;top:1074px;width:560px">One Of The Fastest Way To Gain Business Success</h2>
  <p class="abs body-copy" style="left:591px;top:1167px;width:470px">There are many variations of passages of orem Ipsum available, but the majority have suffered alteration in some form, by cted ipsum dolor sit amet, consectetur adipisicing elit, sed do usmod temporcid idunt ut labore et dolore magna aliqua. Ut enim ad minim veniam, quis nostrud exercitation.</p>
  <div class="abs btn-outline" style="left:589px;top:1295px"><span>READ MORE</span></div>
</section>

<!-- services -->
<section>
  <h2 class="abs section-title" style="top:1455px">Services<br>We're offering</h2>
  <div class="abs service" style="left:164px;top:1703px"><h3>Business Planning</h3><p>There are many variations of passages of orem Ipsum availa-ble, but the majority have suffered alteration in some.</p></div>
  <div class="abs service is-active" style="left:444px;top:1703px"><h3>Market Research</h3><p>There are many variations of passages of orem Ipsum available, but the majority have suffered .</p></div>
  <div class="abs service" style="left:725px;top:1703px"><h3>Grow Business</h3><p>There are many variations of passages of orem Ipsum availa-ble, but the majority have suffered alteration in some.</p></div>
</section>

<!-- consultants -->
<section>
  <div class="abs eyebrow" style="left:158px;top:2061px">Get Solutions Fast</div>
  <h2 class="abs h2" style="left:158px;top:2092px">First Class<br>Consultants</h2>
  <p class="abs body-copy" style="left:158px;top:2184px;width:470px">There are many variations of passages of orem Ipsum available, but the majority have suffered alteration in some form, by cted ipsum dolor sit amet, consectetur adipisicing elit, sed do usmod temporcid idunt ut labore et dolore magna aliqua.</p>
</section>

<!-- stats -->
<section>
  <div class="abs" style="left:169px;top:2545px"><div class="stat-num">90%</div><div class="stat-label">Client Success</div></div>
  <div class="abs" style="left:384px;top:2545px"><div class="stat-num">220+</div><div class="stat-label">Businesses Advised</div></div>
  <div class="abs" style="left:635px;top:2545px"><div class="stat-num">500+</div><div class="stat-label">Guides Given</div></div>
  <div class="abs" style="left:879px;top:2545px"><div class="stat-num">25+</div><div class="stat-label">Awards Achieved</div></div>
</section>

<!-- news -->
<section>
  <h2 class="abs section-title" style="top:2756px">News &amp; Blogs</h2>
  <article class="abs" style="left:146px;top:3072px;width:420px"><div class="news-title">What we are capable to usually discovered.</div><div class="news-desc">Dynamically target high-payoff intellectual capital for customized technologies. Objectively integrate...</div></article>
  <article class="abs" style="left:645px;top:3075px;width:190px"><div class="news-title" style="font-size:19px">What we are capable to usually discovered.</div><div class="news-more">READ MORE</div></article>
  <article class="abs" style="left:898px;top:3075px;width:190px"><div class="news-title" style="font-size:19px">What we are capable to usually discovered.</div><div class="news-more">READ MORE</div></article>
</section>

<!-- partners -->
<section>
  <div class="abs partner" style="left:92px"><i></i>Northvale</div>
  <div class="abs partner" style="left:298px">Brightmoor</div>
  <div class="abs partner" style="left:504px"><i></i>Lumacrest</div>
  <div class="abs partner" style="left:709px">Orbitly</div>
  <div class="abs partner" style="left:914px"><i></i>Veradyn</div>
</section>

<!-- cta -->
<section>
  <div class="abs cta-text">Searching for a First-Class<br>Consultant?</div>
  <div class="abs cta-btn">GET A QUOTE FOAM</div>
</section>

<!-- footer -->
<footer>
  <div class="abs brand footer-brand"><span class="brand-mark"></span><span class="brand-name">SME TIDEWELL</span></div>
  <div class="abs" style="left:415px;top:3745px">
    <div class="f-head">Links</div>
    <ul class="f-list" style="margin-top:4px"><li>Home</li><li>Services</li><li>About us</li><li>Gallery</li><li>Testimonials</li><li>Contact</li><li>News</li></ul>
  </div>
  <div class="abs" style="left:579px;top:3745px">
    <div class="f-head">Newsletter</div>
    <div class="f-list" style="margin-top:4px">Send us a newsletter to get update</div>
  </div>
  <div class="abs f-input">Email Address</div>
  <div class="abs" style="left:873px;top:3745px">
    <div class="f-head">Contact Us</div>
    <ul class="f-list" style="margin-top:4px;padding-left:25px"><li>Some goes address here</li><li>1-555-010-2233</li><li>Open Hours:</li><li>Mon – Sat: 8 am – 5 pm,</li><li>Sunday: CLOSED</li></ul>
  </div>
  <div class="abs social"><i></i><i></i><i></i><i></i></div>
  <div class="abs to-top"></div>
  <svg class="abs" style="left:1121px;top:3995px" width="38" height="38" viewBox="0 0 38 38"><polyline points="12,22 19,15 26,22" fill="none" stroke="#fff" stroke-width="2"/></svg>
  <div class="abs copyright">©Copyright 2022 | All Rights Reserved</div>
</footer>

</body>
</html>
```